Restaurant menu redo

i just want my menu identical to the files i provided. 1 take out menu and 1 dine in menu. i already have both designs with all the items typed in a word document. i need both menus done so i can easily update prices and items in the future. They can be done in either word or illustrator format. I don't need a new design just a identical copy of both menus that i can update and change my self. one menu is a double sided takeout quad fold(legal size). and the other is a dine in 3 individual page menu.

Industry/Entity Type

Restaurant

Requirements
Must have
• i must have the ability to easily edit the menu for future menu and price changes.
Nice to have
• I would like the menu to be as close to the original as possible.

```html
<!DOCTYPE html>
<html lang="en">
<head>
<meta charset="utf-8">
<title>Dine-In Menu</title>
<link href="https://fonts.googleapis.com/css2?family=PT+Sans+Narrow:wght@400;700&display=swap" rel="stylesheet">
<style>
:root{
  --canvas:#ffffff;
  --brick-dark:#b9482a;
  --brick:#d96a3f;
  --brick-light:#e8935f;
  --paper:#f7dfc6;
  --paper-light:#fbeadb;
  --ink:#2b1a12;
  --band-edge:#fff3ee;
  --band-mid:#ef7a5e;
  --band-text:#ffffff;
  --band-outline:#7a2a18;
  --icon:#4a4a4a;
}
*{margin:0;padding:0;box-sizing:border-box}
html,body{width:1200px;height:1200px;overflow:hidden;background:var(--canvas)}
body{font-family:"PT Sans Narrow",sans-serif;color:var(--ink);position:relative}
.menu-page{position:absolute;left:226px;top:21px;width:707px;height:1165px}
.brick-frame{position:absolute;inset:0;background:
  repeating-linear-gradient(0deg,var(--brick) 0 14px,var(--brick-dark) 14px 16px),
  linear-gradient(90deg,var(--brick-light),var(--brick));
  background-blend-mode:multiply}
.parchment{position:absolute;left:38px;top:35px;right:36px;bottom:34px;
  background:radial-gradient(ellipse at center,var(--paper-light) 0%,var(--paper) 80%);
  box-shadow:0 0 18px 10px var(--paper);border-radius:6px}
.band{position:absolute;height:22px;display:flex;align-items:center;justify-content:center;
  background:linear-gradient(90deg,var(--band-edge) 0%,var(--band-mid) 30%,var(--band-mid) 70%,var(--band-edge) 100%);
  font-weight:400;font-size:19px;letter-spacing:.5px;color:var(--band-text);text-transform:uppercase;
  text-shadow:-1px -1px 0 var(--band-outline),1px -1px 0 var(--band-outline),-1px 1px 0 var(--band-outline),1px 1px 0 var(--band-outline)}
.item{position:absolute;text-align:center;transform:translateX(-50%);white-space:nowrap}
.col-left .item{left:192px}
.col-right .item{left:520px}
.col-left,.col-right,.col-desserts,.col-drinks{position:absolute;inset:0}
.item-name{font-weight:700;font-size:13px;line-height:14px}
.item-desc{font-size:9.8px;line-height:11.3px}
.price{font-weight:400;font-size:10px}
.intro{font-style:italic;font-weight:700;font-size:11px;line-height:12px}
.intro .sub{font-weight:400;font-size:9.6px}
.intro .addon{font-style:normal;font-size:10.4px}
.simple .item-name{font-size:13.5px}
.col-desserts .item{left:582px}
.col-desserts .item-name{font-size:13.5px;line-height:14px}
.col-drinks .item{left:335px}
.col-drinks .item-name{font-size:13px}
.col-drinks .item-desc{font-size:9.8px}
.house-icon{display:inline-block;width:15px;height:9px;border-radius:7px 7px 3px 3px;background:var(--icon);margin-right:4px;vertical-align:0}
.beverage-list{position:absolute;left:520px;top:671px;transform:translateX(-50%);text-align:center;font-size:10.4px;line-height:11.2px;white-space:nowrap}
</style>
</head>
<body>
<div class="menu-page">
  <div class="brick-frame" role="img" aria-label="Red brick wall border"></div>
  <div class="parchment"></div>

  <div class="band" style="left:48px;top:51px;width:286px">Pasta Celebrations</div>
  <div class="band" style="left:376px;top:51px;width:286px">Chef Special</div>
  <div class="band" style="left:376px;top:459px;width:286px">Desserts</div>
  <div class="band" style="left:372px;top:638px;width:288px">Beverages</div>
  <div class="band" style="left:192px;top:741px;width:286px">Wine Selection</div>
  <div class="band" style="left:192px;top:894px;width:286px">Beer Selection</div>

  <section class="col-left">
    <div class="item intro" style="top:80px">All served with side house salad &amp; garlic roll<br>
      <span class="sub">Add any of the following to the below pasta dishes:</span><br>
      <span class="addon">Chicken, Meatballs or Sausage <span class="price">4.00</span> • Shrimp <span class="price">5.00</span></span></div>
    <div class="item" style="top:123px"><div class="item-name">Linguini Aioli</div><div class="item-desc">Fresh roasted garlic sautéed in olive oil, tossed with linguini &amp;<br>fresh herbs, sea salt &amp; fresh cracked black pepper. 12.49</div></div>
    <div class="item" style="top:166px"><div class="item-name">Spaghetti ala Marinara</div><div class="item-desc">Homemade marinara sauce tossed with spaghetti. 12.49</div></div>
    <div class="item" style="top:197px"><div class="item-name">Rigatoni ala Vodka</div><div class="item-desc">Sun dried tomatoes, pancetta sautéed, a touch of marinara,<br>cream &amp; a blend of grated cheeses, tossed with rigatoni &amp; fresh basil. 15.99</div></div>
    <div class="item" style="top:239px"><div class="item-name">Broccoli &amp; Garlic</div><div class="item-desc">Broccoli florets &amp; roasted garlic sautéed in olive oil then tossed<br>with bowtie pasta &amp; a blend of grated cheeses. 15.49</div></div>
    <div class="item" style="top:282px"><div class="item-name">Fettuccine Alfredo</div><div class="item-desc">Warm cream, blended with rich egg yolks &amp; a blend of cheese,<br>tossed in fettuccine. 15.49</div></div>
    <div class="item" style="top:324px"><div class="item-name"><span class="house-icon" role="img" aria-label="House favourite icon"></span>Penne ala Fresca</div><div class="item-desc">Fresh plum tomatoes &amp; basil sautéed in olive oil then tossed with<br>penne pasta, butter &amp; a blend of grated cheeses. 13.99</div></div>
    <div class="item" style="top:366px"><div class="item-name">Sausage &amp; Peppers</div><div class="item-desc">Sweet Italian sausage, assorted peppers &amp; onions sautéed in<br>extra virgin olive oil tossed with our homemade marinara sauce,<br>served with a side of pasta. 16.49</div></div>
    <div class="item" style="top:421px"><div class="item-name">Calamari fra Diavolo</div><div class="item-desc">Fresh calamari sautéed with our homemade marinara sauce, garlic, white<br>wine, olive oil, and red pepper flakes then tossed with linguini. 17.49</div></div>
    <div class="item" style="top:463px"><div class="item-name">Linguini with Red or White Clam Sauce</div><div class="item-desc">Hard shell clams &amp; garlic sautéed in olive oil &amp; a splash of white wine<br>&amp; fresh herbs tossed in linguini. 18.49</div></div>
    <div class="item" style="top:506px"><div class="item-name">Mussels Marinara or Bianco</div><div class="item-desc">Mussels &amp; roasted garlic sautéed in olive oil, a splash of white wine<br>&amp; a touch of marina sauce tossed with linguini. 17.49</div></div>
    <div class="item" style="top:548px"><div class="item-name">Shrimp Scampi</div><div class="item-desc">Succulent shrimp sautéed in a garlic, butter and wine sauce<br>served over linguini. 17.49</div></div>
    <div class="item" style="top:590px"><div class="item-name"><span class="house-icon" role="img" aria-label="House favourite icon"></span>Sunday Gravy</div><div class="item-desc">Short ribs, pork shoulder, fresh garlic, celery &amp; carrots sautéed in olive oil,<br>with plum crushed tomatoes, served over parpadelli pasta with a side of</div></div>
    <div class="item simple" style="top:633px"><div class="item-name">Meatballs &amp; sausage <span class="price">17.99</span></div></div>
    <div class="item simple" style="top:653px"><div class="item-name">Baked Lasagna <span class="price">13.99</span></div></div>
    <div class="item simple" style="top:673px"><div class="item-name">Baked Rigatoni <span class="price">13.49</span></div></div>
    <div class="item simple" style="top:692px"><div class="item-name">Baked Manicotti <span class="price">13.49</span></div></div>
    <div class="item simple" style="top:712px"><div class="item-name">Baked Ravioli Dinner <span class="price">13.49</span></div></div>
  </section>

  <section class="col-right">
    <div class="item" style="top:81px"><div class="item-name">Milanese</div><div class="item-desc">Coated with fresh Italian bread crumbs, pan fried in olive oil &amp; served<br>With a side of pasta marinara. <b>Chicken</b> 15.49 | <b>Veal</b> 16.49</div></div>
    <div class="item" style="top:124px"><div class="item-name"><span class="house-icon" role="img" aria-label="House favourite icon"></span>Steak Pizziola</div><div class="item-desc">Pan seared 10 oc. NY strip topped with sautéed peppers &amp; onions then<br>Smothered in freshly homemade marinara sauce. 20.99</div></div>
    <div class="item" style="top:166px"><div class="item-name">Parmesan Encrusted Fillet of Fish</div><div class="item-desc">Topped with Parmesan bread crumbs, butter, white wine &amp; fresh squeezed<br>Lemon, baked &amp; served with vegetables. <b>Tilapia</b> 15.49 | <b>Mahi Mahi</b> 17.49</div></div>
    <div class="item" style="top:210px"><div class="item-name">Broccoli Rabe &amp; Orchetta</div><div class="item-desc">Southern Italian bitter green along with roasted garlic, sautéed &amp; tossed<br>With a blend of cheeses &amp; served with orchetta pasta. 14.99<br><b>Add sausage</b> 4.00</div></div>
    <div class="item" style="top:265px"><div class="item-name">Parmigiana</div><div class="item-desc">Coated with fresh Italian bread crumbs, fried in olive oil then baked with<br>Marinara sauce &amp; mozzarella cheese, served over pasta marinara.<br><b>Chicken</b> 16.49 | <b>Veal</b> 17.49 | <b>Eggplant</b> 15.49</div></div>
    <div class="item" style="top:320px"><div class="item-name">Montreal Steak</div><div class="item-desc">10 oz. NY strip sprinkled with Montreal steak seasoning, cooked to your liking,<br>Served with a side of vegetables &amp; roasted potatoes. 20.99</div></div>
    <div class="item" style="top:362px"><div class="item-name">Fish Dinner</div><div class="item-desc">Our house fish grilled or blackened, served with a<br>side of vegetables &amp; roasted potatoes. 15.49</div></div>
    <div class="item" style="top:405px"><div class="item-name">Chicken Breast Dinner</div><div class="item-desc">Fresh Chicken breast grilled or blackened, served with a<br>Side of vegetables &amp; roasted potatoes. 15.49</div></div>
  </section>

  <section class="col-desserts">
    <div class="item" style="top:496px"><div class="item-name">Homemade Tiramisu <span class="price">5.00</span></div></div>
    <div class="item" style="top:516px"><div class="item-name">Cheesecake <span class="price">5.00</span></div></div>
    <div class="item" style="top:535px"><div class="item-name">Homemade Cannoli <span class="price">3.00</span></div></div>
    <div class="item" style="top:554px"><div class="item-name">Chocolate Cake <span class="price">5.00</span></div></div>
    <div class="item" style="top:574px"><div class="item-name">Apple Pie with<br>Vanilla Bean Ice Cream <span class="price">6.50</span></div></div>
    <div class="item" style="top:608px"><div class="item-name">Cookies &amp; Cream Cake <span class="price">5.00</span></div></div>
  </section>

  <div class="beverage-list">Root beer | Lemon Spark | Lemonade Citrus Peak | Diet Cola<br>House Cola Cherry Cola Fruit Punch Doctor Fizz Sweet Iced Tea<br>Unsweetened Iced Tea Raspberry Iced Tea</div>

  <section class="col-drinks">
    <div class="item" style="top:773px"><div class="item-name">Happy Hour <span class="price">Mon-Fri 4-7</span></div><div class="item-desc">5.00 House Wine 2.00 Domestic Draft 2.50 Domestic Bottle</div></div>
    <div class="item" style="top:804px"><div class="item-name">Harbor Ridge, California: <span class="price">Chardonnay, Pinot Grigio Sauvignon Blanc</span></div><div class="item-desc">White Zinfandel Pinot Noir Merlot Cabernet Sauvignon<br>6.50 Glass|18 Bottle</div></div>
    <div class="item" style="top:847px"><div class="item-name">Chianti<span class="price">, Vallombra, Italy 8 Glass|22 Bottle</span></div></div>
    <div class="item" style="top:867px"><div class="item-name">Sparkling: <span class="price">L.M Durand, France Split 7</span></div></div>
    <div class="item" style="top:934px"><div class="item-name">Domestic: <span class="price">Red Barrel Red Barrel Light Millbrook Lite</span></div><div class="item-desc">Summit Light Meadow Ultra Old Forge</div></div>
    <div class="item" style="top:965px"><div class="item-name">Imports: <span class="price">Bianchi Hollander Hollander Light Playa</span></div><div class="item-desc">Playa Light Lumen Portello</div></div>
    <div class="item" style="top:996px"><div class="item-name">Draft<span class="price">: Millbrook Lite Old Forge Blue Harvest Patriot Seasonal</span></div><div class="item-desc">Black Harp Wide Wheel</div></div>
  </section>
</div>
</body>
</html>
```